2 x storefront vinyl request

We are transitioning to a storefront office and need two vinyls for the windows.

First vinyl: Use the Aldwick Partners logo, website (www.aldwickpartnersestates.example) and leasing office number ((555) 318-4726)

Second vinyl: Maintenance Division & phone number (555) 318-4726

```html
<!DOCTYPE html>
<html lang="en">
<head>
<meta charset="utf-8">
<title>Aldwick Partners – Storefront Window Vinyls</title>
<link rel="stylesheet" href="https://fonts.googleapis.com/css2?family=Montserrat:wght@300;400;600;700&display=swap">
<style>
  :root {
    --backdrop: #a6a6a6;
    --paper: #ffffff;
    --ink: #060709;
    --band-grey: #787876;
    --rule-grey: #b5b5b5;
    --text-light: #ffffff;
  }
  * { box-sizing: border-box; margin: 0; padding: 0; }
  html, body {
    width: 1200px;
    height: 800px;
    overflow: hidden;
    background: var(--backdrop);
    font-family: "Montserrat", Arial, sans-serif;
  }
  .canvas {
    position: relative;
    width: 1200px;
    height: 800px;
  }
  .vinyl {
    position: absolute;
    top: 55px;
    width: 494px;
    height: 688px;
    background: var(--paper);
    overflow: hidden;
  }
  .vinyl--leasing { left: 88px; }
  .vinyl--maintenance { left: 611px; }
  .vinyl__waves {
    position: absolute;
    inset: 0;
    width: 100%;
    height: 100%;
  }
  .wave--grey { fill: var(--band-grey); }
  .wave--black { fill: var(--ink); }

  .brand-name {
    position: absolute;
    left: 96px;
    top: 158px;
    color: var(--ink);
    font-weight: 700;
    font-size: 30px;
    line-height: 33px;
    letter-spacing: 0.5px;
    text-transform: uppercase;
  }

  .leasing-contact {
    position: absolute;
    left: 26px;
    top: 576px;
    color: var(--text-light);
  }
  .leasing-contact__label {
    display: inline-block;
    font-weight: 300;
    font-size: 15px;
    letter-spacing: 1.6px;
    padding-bottom: 3px;
    border-bottom: 1.5px solid var(--rule-grey);
  }
  .leasing-contact__phone {
    font-weight: 700;
    font-size: 31px;
    letter-spacing: 1.5px;
    margin-top: 6px;
    line-height: 36px;
  }
  .leasing-contact__web {
    font-weight: 700;
    font-size: 14.5px;
    letter-spacing: 1.6px;
    margin-top: 8px;
  }

  .maintenance-contact {
    position: absolute;
    right: 26px;
    top: 612px;
    text-align: right;
    color: var(--text-light);
  }
  .maintenance-contact__label {
    display: inline-block;
    font-weight: 700;
    font-size: 18px;
    letter-spacing: 2px;
    padding-bottom: 3px;
    border-bottom: 1.5px solid var(--paper);
  }
  .maintenance-contact__phone {
    font-weight: 700;
    font-size: 26px;
    letter-spacing: 1.5px;
    line-height: 32px;
    margin-top: 6px;
  }
</style>
</head>
<body>
<main class="canvas">

  <section class="vinyl vinyl--leasing" aria-label="Leasing office window vinyl">
    <svg class="vinyl__waves" viewBox="0 0 494 688" aria-hidden="true">
      <path class="wave--grey" d="M0,380 C150,352 320,380 494,514 L494,688 L0,688 Z"/>
      <path class="wave--black" d="M0,427 C150,400 320,430 494,539 L494,688 L0,688 Z"/>
    </svg>
    <h1 class="brand-name">Aldwick<br>Partners<br>Properties</h1>
    <div class="leasing-contact">
      <p class="leasing-contact__label">LEASING OFFICE NUMBER:</p>
      <p class="leasing-contact__phone">(555) 318-4726</p>
      <p class="leasing-contact__web">WWW.ALDWICKPARTNERSESTATES.EXAMPLE</p>
    </div>
  </section>

  <section class="vinyl vinyl--maintenance" aria-label="Maintenance division window vinyl">
    <svg class="vinyl__waves" viewBox="0 0 494 688" aria-hidden="true">
      <path class="wave--grey" d="M494,393 Q300,455 116,598 L8,688 L22,688 L128,608 Q300,480 494,434 Z"/>
      <path class="wave--black" d="M494,434 Q300,485 126,612 L222,688 L494,688 Z"/>
      <path class="wave--grey" d="M0,515 Q60,552 116,596 L230,688 L216,688 L108,606 Q60,568 0,530 Z"/>
      <path class="wave--black" d="M0,530 Q60,568 108,606 L14,688 L0,688 Z"/>
    </svg>
    <div class="maintenance-contact">
      <p class="maintenance-contact__label">MAINTENANCE DIVISION</p>
      <p class="maintenance-contact__phone">(555) 318-4726</p>
    </div>
  </section>

</main>
</body>
</html>
```